Vorential Health Posters

Two posters needed to introduce our new package pricing, called our SPARK and GLOW programs. Our current posters are attached, these two new posters should be similar design and layout. The docx attached has what information should be on each poster. (vorentialhealth.com)

```html
<!DOCTYPE html>
<html lang="en">
<head>
<meta charset="utf-8">
<title>Vorential Health – GLOW Package Poster</title>
<link rel="stylesheet" href="https://fonts.googleapis.com/css2?family=Outfit:wght@400;500;600;700&display=swap">
<style>
  :root {
    --page-bg: #2b2d32;
    --poster-bg: #141416;
    --poster-bg-light: #222226;
    --brand-red: #e0151f;
    --text-white: #ffffff;
    --text-soft: #d9d9dc;
    --pill-bg: rgba(255,255,255,0.07);
    --photo-dark: #2c2f36;
    --photo-mid: #6b6f78;
  }
  * { box-sizing: border-box; margin: 0; padding: 0; }
  html, body {
    width: 1200px; height: 803px; overflow: hidden;
    background: var(--page-bg);
    font-family: "Outfit", sans-serif;
  }
  .stage {
    width: 1200px; height: 803px;
    display: flex; align-items: center; justify-content: center;
  }
  .poster {
    position: relative;
    width: 430px; height: 740px;
    overflow: hidden;
    background: linear-gradient(160deg, var(--poster-bg-light) 0%, var(--poster-bg) 55%, #0d0d0f 100%);
    color: var(--text-white);
  }
  .package-label {
    position: absolute; left: 16px; top: 80px;
    color: var(--brand-red);
    font-weight: 700; font-size: 20px; line-height: 1.05;
    text-transform: uppercase;
  }
  .brand {
    position: absolute; right: 24px; top: 66px;
    display: flex; align-items: center; gap: 8px;
  }
  .brand-dot {
    width: 14px; height: 14px; border-radius: 50%;
    background: var(--brand-red);
  }
  .brand-name {
    font-weight: 600; font-size: 15px; color: var(--brand-red);
  }
  .headline {
    position: absolute; left: 16px; top: 150px;
    font-weight: 600; font-size: 39px; line-height: 1.08;
    letter-spacing: -0.5px;
  }
  .hero {
    position: absolute; left: 225px; top: 180px;
    width: 410px; height: 410px;
  }
  .benefits {
    position: absolute; left: 16px; top: 378px;
    list-style: none;
    display: flex; flex-direction: column; gap: 11px;
  }
  .benefit {
    display: flex; align-items: center;
    height: 26px; padding: 0 10px 0 0;
    background: var(--pill-bg);
    border-radius: 13px;
    font-size: 19px; font-weight: 400; color: var(--text-soft);
  }
  .benefit::before {
    content: ""; width: 6px; height: 26px;
    background: var(--brand-red);
    border-radius: 13px 0 0 13px;
    margin-right: 8px;
  }
  .powered-tag {
    position: absolute; left: 16px; top: 574px;
    background: var(--brand-red);
    border-radius: 10px;
    padding: 2px 12px;
    font-size: 11px; font-weight: 400;
  }
  .offer {
    position: absolute; left: 18px; top: 606px;
    font-weight: 700; font-size: 19px; line-height: 1.22;
    text-transform: uppercase;
  }
  .offer-note {
    position: absolute; left: 18px; top: 664px;
    font-size: 14px; font-weight: 400; color: var(--text-soft);
  }
  .offer-note strong { font-weight: 700; color: var(--text-white); }
</style>
</head>
<body>
<main class="stage">
  <article class="poster">
    <p class="package-label">Glow<br>Package</p>

    <div class="brand">
      <span class="brand-dot"></span>
      <span class="brand-name">Vorential Health</span>
    </div>

    <h1 class="headline">Burn Fat. Boost<br>Energy.<br>Transform<br>Your Body.</h1>

    <svg class="hero" viewBox="0 0 410 410" role="img" aria-label="Photo of a muscular man lifting a dumbbell inside a red ring">
      <defs>
        <radialGradient id="heroFill" cx="45%" cy="45%" r="60%">
          <stop offset="0%" stop-color="var(--photo-mid)"/>
          <stop offset="100%" stop-color="var(--photo-dark)"/>
        </radialGradient>
      </defs>
      <circle cx="205" cy="205" r="198" fill="#b9141b"/>
      <circle cx="214" cy="205" r="186" fill="url(#heroFill)"/>
    </svg>

    <ul class="benefits">
      <li class="benefit">Increase Fat Loss</li>
      <li class="benefit">Boost Metabolism</li>
      <li class="benefit">Improve Sleep</li>
      <li class="benefit">Protect Muscle Mass</li>
      <li class="benefit">Increase Energy</li>
    </ul>

    <p class="powered-tag">Powered by Peptides – TRT</p>

    <p class="offer">One Low Monthly Price<br>Save Big Over The Year</p>
    <p class="offer-note">3 Months <strong>FREE</strong> When You Stay Committed All Year</p>
  </article>
</main>
</body>
</html>
```